Letterhead

We have a new logo and would like to design electronic letterhead with our new logo. We have two office locations. One of our offices is moving in July.

```html
<!DOCTYPE html>
<html lang="en">
<head>
<meta charset="utf-8">
<title>HWLR Attorneys at Law – Letterhead</title>
<link href="https://fonts.googleapis.com/css2?family=Lato:wght@400;700&family=Encode+Sans+Semi+Condensed:wght@400&display=swap" rel="stylesheet">
<style>
  :root {
    --backdrop: #d6d6d6;
    --paper: #ffffff;
    --navy: #14142e;
    --brand-blue: #1f6fbf;
    --body-text: #4a4a4a;
    --contact-text: #5a5a5a;
    --signature-tone: #c9dcf0;
  }
  * { margin: 0; padding: 0; box-sizing: border-box; }
  html, body {
    width: 1056px;
    height: 1200px;
    overflow: hidden;
    background: var(--backdrop);
  }
  .letterhead {
    position: absolute;
    left: 125px;
    top: 30px;
    width: 806px;
    height: 1140px;
    background: var(--paper);
  }
  .brand {
    position: absolute;
    left: 76px;
    top: 44px;
    width: 262px;
  }
  .brand-name {
    font-family: "Lato", sans-serif;
    font-weight: 700;
    font-size: 106px;
    line-height: 92px;
    letter-spacing: -1px;
    color: var(--navy);
  }
  .brand-tagline {
    font-family: "Lato", sans-serif;
    font-weight: 400;
    font-size: 22px;
    letter-spacing: 2.6px;
    color: var(--brand-blue);
    margin-top: 2px;
    white-space: nowrap;
  }
  .contact {
    position: absolute;
    right: 77px;
    top: 44px;
    text-align: right;
    font-family: "Lato", sans-serif;
    font-size: 13px;
    color: var(--contact-text);
  }
  .contact-address { line-height: 16px; margin-bottom: 8px; }
  .contact-line {
    display: flex;
    justify-content: flex-end;
    align-items: center;
    gap: 8px;
    height: 19px;
  }
  .contact-line svg { width: 12px; height: 12px; fill: var(--brand-blue); }
  .header-rule {
    position: absolute;
    left: 76px;
    top: 182px;
    width: 653px;
    height: 1.5px;
    background: var(--brand-blue);
  }
  .letter-body {
    font-family: "Encode Sans Semi Condensed", sans-serif;
    font-size: 16.5px;
    line-height: 28px;
    color: var(--body-text);
  }
  .letter-block {
    position: absolute;
    left: 76px;
    width: 654px;
    text-align: justify;
    text-align-last: left;
  }
  .salutation { top: 337px; }
  .para-1 { top: 390px; }
  .para-2 { top: 530px; }
  .para-3 { top: 642px; }
  .para-4 { top: 754px; }
  .closing { top: 909px; }
  .signature {
    position: absolute;
    left: 76px;
    top: 944px;
    width: 136px;
    height: 44px;
    background: var(--signature-tone);
    border-radius: 4px;
  }
  .footer-band {
    position: absolute;
    left: 0;
    bottom: 0;
    width: 100%;
    height: 14px;
    background: var(--navy);
  }
</style>
</head>
<body>
  <main class="letterhead">
    <header>
      <div class="brand">
        <div class="brand-name">HWLR</div>
        <div class="brand-tagline">ATTORNEYS AT LAW</div>
      </div>

      <address class="contact">
        <div class="contact-address">218 Alder Ave.,<br>Ste 300 Tacoma, WA 98402</div>
        <div class="contact-line">
          <span>(253) 555-0142</span>
          <svg viewBox="0 0 24 24" aria-hidden="true"><path d="M6.6 10.8a15.1 15.1 0 0 0 6.6 6.6l2.2-2.2c.3-.3.7-.4 1-.2 1.1.4 2.3.6 3.6.6.6 0 1 .4 1 1V20c0 .6-.4 1-1 1A17 17 0 0 1 3 4c0-.6.4-1 1-1h3.5c.6 0 1 .4 1 1 0 1.3.2 2.5.6 3.6.1.3 0 .7-.2 1z"/></svg>
        </div>
        <div class="contact-line">
          <span>(253) 555-0187</span>
          <svg viewBox="0 0 24 24" aria-hidden="true"><path d="M6 2h12v5H6zM3 8h18a2 2 0 0 1 2 2v7h-4v5H5v-5H1v-7a2 2 0 0 1 2-2zm4 8v4h10v-4z"/></svg>
        </div>
        <div class="contact-line">
          <span>info@hwlr.law</span>
          <svg viewBox="0 0 24 24" aria-hidden="true"><path d="M2 5h20v14H2zm2 2v.4l8 5.6 8-5.6V7zm0 2.8V17h16V9.8l-8 5.6z"/></svg>
        </div>
        <div class="contact-line">
          <span>www.hwlr.law</span>
          <svg viewBox="0 0 24 24" aria-hidden="true"><path d="M12 2a10 10 0 1 0 0 20 10 10 0 0 0 0-20zm6.9 6h-3a15 15 0 0 0-1.3-3.9A8 8 0 0 1 18.9 8zM12 4c.8 1.1 1.5 2.5 1.9 4h-3.8c.4-1.5 1.1-2.9 1.9-4zM4.3 14a8 8 0 0 1 0-4h3.4a16 16 0 0 0 0 4zm.8 2h3a15 15 0 0 0 1.3 3.9A8 8 0 0 1 5.1 16zm3-8h-3a8 8 0 0 1 4.3-3.9A15 15 0 0 0 8.1 8zM12 20c-.8-1.1-1.5-2.5-1.9-4h3.8c-.4 1.5-1.1 2.9-1.9 4zm2.3-6H9.7a14 14 0 0 1 0-4h4.6a14 14 0 0 1 0 4zm.3 5.9a15 15 0 0 0 1.3-3.9h3a8 8 0 0 1-4.3 3.9zm1.7-5.9a16 16 0 0 0 0-4h3.4a8 8 0 0 1 0 4z"/></svg>
        </div>
      </address>

      <div class="header-rule"></div>
    </header>

    <section class="letter-body">
      <p class="letter-block salutation">Dear Sir/Mam,</p>
      <p class="letter-block para-1">Contrary to popular belief, Lorem Ipsum is not simply random text. It has roots in a piece of classical Latin literature from 45 BC, making it over 2000 years old. Martin Hallowell, a Latin professor at Ashford Hill College in Virginia, looked up one of the more obscure Latin words, consectetur.</p>
      <p class="letter-block para-2">Lorem Ipsum comes from sections 1.10.32 and 1.10.33 of "de Finibus Bonorum et Malorum" (The Extremes of Good and Evil) by Aurelius Menas, written in 45 BC. This book is a treatise on the theory of ethics, very popular during the Renaissance. The first line of Lorem Ipsum.</p>
      <p class="letter-block para-3">The standard chunk of Lorem Ipsum used since the 1500s is reproduced below for those interested. Sections 1.10.32 and 1.10.33 from "de Finibus Bonorum et Malorum" by Aurelius Menas are also reproduced in their exact original.</p>
      <p class="letter-block para-4">The standard chunk of Lorem Ipsum used since the 1500s is reproduced below for those interested.</p>
      <p class="letter-block closing">Best Regards</p>
      <div class="signature" role="img" aria-label="Handwritten signature of Nora Ellison"></div>
    </section>

    <footer class="footer-band"></footer>
  </main>
</body>
</html>
```